New Infusion Pharmacy needs Business Card design

Hello!

We are Meridale Infusion Pharmacy, are we are looking for a two sided, clean and modern business card.

First, let me give you a little bit about what an infusion pharmacy does...
We compound and fill prescriptions for drugs that are injectable, meaning that they are administered via an IV bag or a syringe. Basically anything that is too advanced for a normal pill pharmacy to fill. We compound everything in our state of the art clean room, then deliver it directly to the patients home. We have an outside sales force that markets to hospitals, home health agencies, and doctor's offices.

as for the business card...
We are looking for a clean, modern card. our colors are in our logo, kind of a light bule and a darker blue. We do really like the rounded corners on the card. Also, we would like the back of the card to be the reverse colors of the front, for example, if the front of the card has a light background, then the back of the card will have a dark background.

On the back side of the card we want to have our logo, then list some of the services we offer:
-IVIG
-TPN
-Enteral Nutrition
-IV Antibiotics
-IV Hydration
-Blood Factors
-Chemotherapy
-Pain Management

Our logo is uploaded in .psd format, if you need a different format let me know and i'll throw it up here.

Thank you so much!!

Industry/Entity Type

Pharmacy

Requirements
Must have
• Front of Card: (no particular order, please arrange in whatever way you think looks best!)
-Employee Name
-Title
-Office Phone #
-Cell Phone #
-Fax #
-email address - tobin@meridaleinfusion-example.com
-office address - 4127 Harlow St. Cypress, CA 90630
-Web Site - www.meridaleinfusion-example.com

```html
<!DOCTYPE html>
<html lang="en">
<head>
<meta charset="utf-8">
<title>Meridale Infusion Pharmacy – Business Card</title>
<link rel="stylesheet" href="https://fonts.googleapis.com/css2?family=Source+Sans+3:wght@400;600&display=swap">
<style>
  :root {
    --stage: #e9e6e2;
    --teal-light: #1aa0c4;
    --teal-mid: #137f9d;
    --teal-dark: #0b566c;
    --ink: #0f4f63;
    --accent: #1795bd;
    --white: #ffffff;
  }
  * { box-sizing: border-box; margin: 0; padding: 0; }
  html, body { width: 1200px; height: 836px; overflow: hidden; }
  body {
    background: var(--stage);
    font-family: "Source Sans 3", "Myriad Pro", Arial, sans-serif;
    position: relative;
  }
  .card {
    position: absolute;
    width: 500px;
    height: 278px;
    border-radius: 18px;
    overflow: hidden;
    box-shadow: 0 6px 18px rgba(0,0,0,0.18);
  }

  /* Front */
  .card--front { left: 350px; top: 70px; background: var(--white); }
  .front__top-band { position: absolute; left: 0; top: 0; width: 100%; height: 16px; background: var(--teal-light); }
  .front__bottom-band {
    position: absolute; left: 0; bottom: 0; width: 100%; height: 32px;
    background: var(--teal-dark); color: var(--white);
    font-size: 13px; text-align: center; line-height: 32px;
  }
  .front__person { position: absolute; left: 50px; top: 54px; font-size: 14px; line-height: 19px; }
  .person__name { color: var(--ink); }
  .person__title { color: var(--accent); }
  .front__brand {
    position: absolute; right: 30px; top: 50px; text-align: right;
    color: var(--ink); font-weight: 600; line-height: 1;
  }
  .brand__main { font-size: 34px; letter-spacing: 1px; display: block; }
  .brand__sub { font-size: 10px; letter-spacing: 3.4px; display: block; margin-top: 3px; }
  .front__address {
    position: absolute; left: 34px; top: 181px;
    font-size: 13px; line-height: 17px; color: var(--ink);
  }
  .front__phones {
    position: absolute; right: 28px; top: 181px;
    font-size: 13px; line-height: 17px; color: var(--ink);
  }

  /* Backs */
  .card--back {
    background: radial-gradient(ellipse at 52% 40%, var(--teal-light) 0%, var(--teal-mid) 45%, var(--teal-dark) 100%);
    color: var(--white);
  }
  .card--back-a { left: 70px; top: 460px; }
  .card--back-b { left: 630px; top: 460px; }
  .back-a__services { position: absolute; left: 36px; top: 58px; font-size: 15px; }
  .services__heading { font-size: 17px; margin-bottom: 10px; }
  .services__list { list-style: none; font-size: 14px; line-height: 18px; padding-left: 10px; }
  .services__list li::before { content: "* "; }
  .back-a__brand { position: absolute; right: 34px; top: 118px; text-align: right; font-weight: 600; line-height: 1; }
  .back-b__brand { position: absolute; left: 0; width: 100%; top: 52px; text-align: center; font-weight: 600; line-height: 1; }
  .brand--light .brand__main { font-size: 38px; }
  .brand--light .brand__sub { font-size: 10px; letter-spacing: 3.8px; margin-top: 4px; }
  .back-b__heading {
    position: absolute; left: 0; width: 100%; top: 128px; text-align: center;
    font-size: 16px; text-decoration: underline; text-underline-offset: 3px; letter-spacing: 0.5px;
  }
  .back-b__col { position: absolute; top: 168px; }
  .back-b__col--1 { left: 40px; top: 206px; }
  .back-b__col--2 { left: 190px; }
  .back-b__col--3 { left: 350px; top: 160px; }
</style>
</head>
<body>

<section class="card card--front" aria-label="Business card front">
  <div class="front__top-band"></div>
  <div class="front__person">
    <p class="person__name">Your Name Here</p>
    <p class="person__title">Designation</p>
  </div>
  <div class="front__brand">
    <span class="brand__main">MERIDALE</span>
    <span class="brand__sub">INFUSION PHARMACY</span>
  </div>
  <div class="front__address">
    <p>4127 Harlow St. Cypress, CA 90630</p>
    <p>E: tobin@meridaleinfusion-example.com</p>
    <p>W: www.meridaleinfusion-example.com</p>
  </div>
  <div class="front__phones">
    <p>M: (000) 555-0126</p>
    <p>T: (808) 555-0142</p>
    <p>F: (808) 555-0178</p>
  </div>
  <div class="front__bottom-band">www.meridaleinfusion-example.com</div>
</section>

<section class="card card--back card--back-a" aria-label="Business card back, list layout">
  <div class="back-a__services">
    <p class="services__heading">Services We Offer:</p>
    <ul class="services__list">
      <li>IVIG</li>
      <li>TPN</li>
      <li>Enteral Nutrition</li>
      <li>IV Antibiotics</li>
      <li>IV Hydration</li>
      <li>Blood Factors</li>
      <li>Chemotherapy</li>
      <li>Pain Management</li>
    </ul>
  </div>
  <div class="back-a__brand brand--light">
    <span class="brand__main">MERIDALE</span>
    <span class="brand__sub">INFUSION PHARMACY</span>
  </div>
</section>

<section class="card card--back card--back-b" aria-label="Business card back, centred layout">
  <div class="back-b__brand brand--light">
    <span class="brand__main">MERIDALE</span>
    <span class="brand__sub">INFUSION PHARMACY</span>
  </div>
  <p class="back-b__heading">SERVICES WE OFFER</p>
  <ul class="services__list back-b__col back-b__col--1">
    <li>IVIG</li>
    <li>IV Antibiotics</li>
    <li>Chemotherapy</li>
  </ul>
  <ul class="services__list back-b__col back-b__col--2">
    <li>TPN</li>
    <li>IV Hydration</li>
    <li>Pain Management</li>
  </ul>
  <ul class="services__list back-b__col back-b__col--3">
    <li>Enteral Nutrition</li>
    <li>Blood Factors</li>
  </ul>
</section>

</body>
</html>
```